Presentation for ICS Security Powerpoint Slide Animations

I need to animate my powerpoint and really need the creative imagination and rendition of the concept presented on each slide. The powerpoint slide I will be uploading soon needs to be viewed in presentation mode so that you are able to get the idea of the sequence of appearance of the objects. Also, please read the notes embedded on each of the powerpoint slides so that you can have an idea what I have in mind that needs to be portrayed. The theme of this entire presentation is about industrial control systems security. It contains elements of IT technologies, as well as standard industrial RISK management objects. So for elements pertaining to: for example, the shutting down of a processing plant - I would like to request that the object and the associated animation that portrays this 2 second flash to show the processing plant breaking and coming to a halt. I indicated in one of my slides that the shutdown of this plant causes financial loss - so for this rendition, I need a graphic rendition of a business losing money. It could for example portrayed as "Dollars flying away out of the bank and the business going broke" for example. There are many of these scenarios and situations that I need your imagination to portray. I will be uploading soon. Thanks.

Dear Graphic Designers, I just uploaded the powerpoint file that contains the skeleton presentation. Please read all the notes, and then view the powerpoint in presentation mode to get the look and feel of the sequence and timing of animations. Please also note that whatever graphic I have depicted here is a basic graphic. I am looking for somebody who can render the graphic in a more dramatic manner, combination of graphic animations. I have included for notes on most of the slides to give you guidance. For some of the slides that did not have any notes, I am asking you to render the graphic in that slide following the same concept. Thanks. Added Saturday, March 11, 2017

Dear Graphic Designers, Please note the following:1. Go ahead and remove the words Brantel Plant Systems Defence Summit and Expo Title on the title page. 2. Also, if I may suggest, the water mark design on the title slide, I would like to see elements of computers, a refining or processing plant with pump jacks, valves, motors showing connectivity back to the computers. And perhaps some grayed out wordings like - intrusion detection, firewalls, security monitoring, security incident event. monitoring. Maybe elements of a vault with a dial mechanism for a lock. Something like that would be nice. 3. The theme around this is Industrial Control System security so it pertains to an industrial environment and the security around it. As a suggestion, if you could look up industrial control system security in the web, there are actually a lot of materials on it. Look for one that depicts a network diagram of one and you will see how the valves, motors, and pumps (for example), connect back to computers that control the entire processing plant. Thanks again Added Saturday, March 11, 2017

ICS Security Presentation

Computer Security

Sans Serif

• animated objects that pop up and shows in sequence. Must be compatible to run with a Microsoft Powerpoint application. Must be original versus clipart images.
• Flash audio (only it is compatible to play with Powerpoint?) Original graphic depiction.
• Cut and pasted pictures.

```html
<!DOCTYPE html>
<html lang="en">
<head>
<meta charset="utf-8">
<title>Implementing A Comprehensive and Sustainable ICS Security Framework</title>
<link rel="stylesheet" href="https://fonts.googleapis.com/css2?family=Raleway:wght@300;400;700&display=swap">
<style>
  :root {
    --page: #ffffff;
    --slide-blue-deep: #1d5d8f;
    --slide-blue: #2f6fa3;
    --slide-blue-light: #4b88b9;
    --panel-blue: rgba(40, 104, 164, 0.94);
    --wire-dark: #1a1818;
    --wire-mid: #3a3432;
    --wire-warm: #5a4038;
    --text-light: #ffffff;
    --text-faint: rgba(255, 255, 255, 0.2);
    --sign-paper: #f1f0ee;
    --sign-ink: #1c1c1c;
  }
  * { box-sizing: border-box; margin: 0; padding: 0; }
  html, body {
    width: 1200px;
    height: 3000px;
    overflow: hidden;
    background: var(--page);
  }
  body { position: relative; font-family: "Raleway", sans-serif; }

  .slide {
    position: absolute;
    left: 12px;
    width: 1176px;
    height: 882px;
    overflow: hidden;
    box-shadow: 0 6px 18px rgba(0, 0, 0, 0.35);
  }

  /* Title slide */
  .slide--title { top: 310px; }
  .title-backdrop {
    position: absolute;
    inset: 0;
    background:
      radial-gradient(circle at 52% 38%, rgba(150, 200, 235, 0.35) 0, rgba(150, 200, 235, 0) 32%),
      linear-gradient(160deg, var(--slide-blue-light) 0%, var(--slide-blue) 45%, var(--slide-blue-deep) 100%);
  }
  .watermark-word {
    position: absolute;
    font-weight: 300;
    font-size: 66px;
    color: var(--text-faint);
    white-space: nowrap;
    line-height: 1;
  }
  .title-text {
    position: absolute;
    right: 64px;
    top: 474px;
    text-align: right;
    color: var(--text-light);
    font-size: 73px;
    line-height: 88px;
    font-weight: 300;
    letter-spacing: -0.5px;
    white-space: nowrap;
  }
  .title-text strong { font-weight: 700; }

  /* Question slide */
  .slide--question { top: 1234px; }
  .cabling-backdrop {
    position: absolute;
    inset: 0;
    background:
      radial-gradient(ellipse at 25% 20%, rgba(120, 110, 100, 0.35) 0, rgba(0,0,0,0) 45%),
      linear-gradient(180deg, var(--wire-mid) 0%, var(--wire-warm) 30%, var(--wire-dark) 100%);
  }
  .warning-sign {
    position: absolute;
    left: 84px;
    top: 124px;
    width: 206px;
    height: 200px;
    background: var(--sign-paper);
    color: var(--sign-ink);
    font-size: 26px;
    line-height: 32px;
    text-align: center;
    padding-top: 50px;
    transform: rotate(-1.5deg);
    box-shadow: 0 2px 6px rgba(0, 0, 0, 0.4);
  }
  .question-panel {
    position: absolute;
    left: 588px;
    top: 222px;
    width: 554px;
    height: 500px;
    background: var(--panel-blue);
    color: var(--text-light);
    display: flex;
    align-items: center;
    justify-content: center;
    text-align: center;
    font-weight: 300;
    font-size: 73px;
    line-height: 86px;
  }
</style>
</head>
<body>

  <section class="slide slide--title">
    <div class="title-backdrop" role="img" aria-label="Blue technology backdrop with a faint globe, wifi, padlock and home network icons"></div>
    <span class="watermark-word" style="left:32px; top:88px;">Intrusion</span>
    <span class="watermark-word" style="left:232px; top:166px;">detection</span>
    <span class="watermark-word" style="left:722px; top:106px;">firewalls</span>
    <span class="watermark-word" style="left:628px; top:288px;">security</span>
    <span class="watermark-word" style="left:788px; top:362px;">monitoring</span>
    <span class="watermark-word" style="left:36px; top:356px;">security</span>
    <span class="watermark-word" style="left:84px; top:432px;">incident event</span>
    <h1 class="title-text">
      Implementing A<br>
      Comprehensive and<br>
      <strong>Sustainable</strong><br>
      <strong>ICS Security Framework</strong>
    </h1>
  </section>

  <section class="slide slide--question">
    <div class="cabling-backdrop" role="img" aria-label="Photo of a server rack overflowing with tangled network cables"></div>
    <p class="warning-sign">Do not touch<br>any of these<br>wires</p>
    <h2 class="question-panel">What<br>happens if<br>the sign falls<br>off?</h2>
  </section>

</body>
</html>
```